University of Carrowmere Lindell Saxophone Quartet Concert

We need a poster design advertising the Lindell Saxophone Quartet Concert on Tuesday, April 23 at 5pm. The program concert will consist of 2 works by Peter Voskuilen: Harbor Lanterns and Meridian ledger. These two works should be included on the poster being the concert is featuring the composer and his works. Peter Voskuilen is known for his very "natural" sounding music. He resides in Montana and writes mostly from his small cottage in the mountains. This same idea of nature and "Montana" should be included on the poster design. He is deeply influenced by Thrane and most of the music he writes is play offs from Thrane Chorales.

The concert title is: "Where Stillness Gathers Near"

Target Market(s)

Collegiate Musician, Professional Musicians, Music Faculty

Industry/Entity Type

Advertising

Requirements
Must have
• 1. Title of the Concert: "Where Stillness Gathers Near"
2. "Lindell Saxophone Quartet Presents"
3. Date (April 23)
4. Time: 5pm
5. Location: Chapel of The Gentle Osric
Nice to have
• Nice to maybe keep the idea of "Montana" and that mountian-esque feel

```html
<!DOCTYPE html>
<html lang="en">
<head>
<meta charset="utf-8">
<title>Where Stillness Gathers Near — Lindell Saxophone Quartet</title>
<link rel="stylesheet" href="https://fonts.googleapis.com/css2?family=Anton&display=swap">
<style>
  :root {
    --page: #ffffff;
    --mustard: #dfab29;
    --charcoal: #323132;
    --ink: #231f20;
    --paper: #ffffff;
    --instrument-tone: #4d4d50;
  }
  * { margin: 0; padding: 0; box-sizing: border-box; }
  html, body {
    width: 1200px;
    height: 900px;
    overflow: hidden;
    background: var(--page);
  }
  .canvas {
    position: relative;
    width: 1200px;
    height: 900px;
  }
  .poster {
    position: absolute;
    left: 287px;
    top: 20px;
    width: 606px;
    height: 858px;
    background: var(--mustard);
    overflow: hidden;
    font-family: "Anton", "Impact", sans-serif;
  }
  .hillside {
    position: absolute;
    left: 0;
    top: 0;
    width: 606px;
    height: 858px;
  }
  .instrument-area {
    position: absolute;
    left: 18px;
    top: 555px;
    width: 340px;
    height: 303px;
    background: linear-gradient(180deg, var(--instrument-tone) 0%, rgba(77,77,80,0.55) 100%);
    border-radius: 4px;
  }
  .header {
    position: absolute;
    right: 30px;
    top: 30px;
    text-align: right;
    color: var(--ink);
    text-transform: uppercase;
  }
  .presenter {
    font-size: 33px;
    line-height: 1;
    letter-spacing: 0.5px;
    transform: scaleY(1.05);
  }
  .title-lead {
    margin-top: 10px;
    font-size: 56px;
    line-height: 1;
  }
  .title-close {
    margin-top: 12px;
    font-size: 86px;
    line-height: 1;
  }
  .when {
    position: absolute;
    left: 46px;
    top: 322px;
    color: var(--paper);
    line-height: 1;
  }
  .when .day { font-size: 36px; text-transform: uppercase; }
  .when .date { font-size: 44px; margin-top: 6px; }
  .when .time { font-size: 70px; margin-top: 4px; }
  .venue {
    position: absolute;
    right: 30px;
    top: 566px;
    text-align: right;
    color: var(--paper);
    font-size: 80px;
    line-height: 1.05;
  }
</style>
</head>
<body>
<div class="canvas">
  <div class="poster">
    <svg class="hillside" viewBox="0 0 606 858" role="img" aria-label="Dark mountain slope silhouette with pine trees and an elk standing on the ridge">
      <path d="M0 210 C40 200 100 205 160 262 C210 310 260 400 330 462 C380 500 460 508 606 520 L606 858 L0 858 Z" fill="var(--charcoal)"/>
    </svg>

    <div class="instrument-area" role="img" aria-label="Faint grey silhouettes of three saxophones and a clarinet"></div>

    <header class="header">
      <p class="presenter">Lindell Saxophone Quartet Presents</p>
      <h1>
        <span class="title-lead" style="display:block">Where Stillness</span>
        <span class="title-close" style="display:block">Gathers Near</span>
      </h1>
    </header>

    <div class="when">
      <p class="day">Tuesday</p>
      <p class="date">April 23</p>
      <p class="time">5pm</p>
    </div>

    <p class="venue">Chapel<br>of the<br>Gentle Osric</p>
  </div>
</div>
</body>
</html>
```